Marwick Estate Services (Handyman / Home Improvement Company)

Looking for a double sided professional looking business card with Logo attached to be highlighted on one side and throwing in an image of a handyman as an option would be nice to see as well. We are a company focused on providing quality Handyman and Home improvement services in a timely manner that is done right the first time with integrity

Industry/Entity Type

Handyman / Home Improvement

Contact Information for Business Card

(LOGO, Name, Mobile and office phone numbers, email) on front side of card, (the words "The SOLUTION to all of your Handyman and Home Improvement needs" followed by "Family Owned and Operated" at the very bottom) on the back.

Colors
EB3D1F
EC4F4E
F09395
F8D3D4
FCEDEE

Requirements
Must have
• Red, Gray, Black Color scheme
Should not have
• No Yellow or Blue colors

```html
<!DOCTYPE html>
<html lang="en">
<head>
<meta charset="utf-8">
<title>Marwick Estate Services — Business Card</title>
<link rel="stylesheet" href="https://fonts.googleapis.com/css2?family=Antonio:wght@700&family=Archivo:wght@800&family=Poppins:wght@400&display=swap">
<style>
  :root {
    --red: #e92c30;
    --red-line: #ec4f4e;
    --ink: #1c1c1c;
    --white: #ffffff;
    --backdrop: #9c9c9c;
    --rule-light: #f8d3d4;
  }
  * { box-sizing: border-box; margin: 0; padding: 0; }
  html, body {
    width: 1093px; height: 1200px; overflow: hidden;
    background: var(--backdrop);
  }
  .canvas { position: relative; width: 1093px; height: 1200px; }

  .card {
    position: absolute; left: 264px;
    width: 580px; height: 356px;
    border-radius: 24px; overflow: hidden;
  }
  .card--front { top: 226px; background: var(--white); }
  .card--back { top: 621px; background: var(--red); }

  /* Front */
  .brand {
    position: absolute; left: 303px; top: 40px; width: 230px;
    display: flex; flex-direction: column; align-items: center; gap: 10px;
    font-family: "Archivo", Arial, sans-serif; font-weight: 800;
    color: var(--red); text-align: center; line-height: 1.05;
  }
  .brand__dot { width: 44px; height: 44px; border-radius: 50%; background: var(--red); }
  .brand__name { font-size: 25px; letter-spacing: 0.5px; }

  .holder {
    position: absolute; left: 33px; top: 202px;
    font-family: "Archivo", Arial, sans-serif; font-weight: 800;
    font-size: 24px; color: var(--red); letter-spacing: 0.2px;
  }
  .holder-rule {
    position: absolute; left: 34px; top: 234px; width: 512px; height: 1px;
    background: var(--red-line);
  }
  .contacts {
    position: absolute; left: 33px; top: 250px; list-style: none;
    font-family: "Poppins", Arial, sans-serif; font-size: 17.5px; color: var(--ink);
  }
  .contacts li { display: flex; align-items: center; height: 22px; }
  .contacts svg { width: 15px; height: 15px; margin-right: 7px; fill: var(--red); flex: none; }
  .front-band {
    position: absolute; left: 0; bottom: 0; width: 100%; height: 12px; background: var(--red);
  }

  /* Back */
  .slogan {
    position: absolute; left: 0; top: 52px; width: 100%;
    font-family: "Antonio", "Arial Narrow", sans-serif; font-weight: 700;
    color: var(--white); text-align: center; text-transform: uppercase;
    text-shadow: 1px 2px 2px rgba(0,0,0,0.25);
  }
  .slogan__lead { display: block; font-size: 42px; line-height: 58px; }
  .slogan__main { display: block; font-size: 60px; line-height: 74px; }
  .tagline {
    position: absolute; left: 0; top: 300px; width: 100%;
    display: flex; align-items: center; gap: 8px;
    font-family: "Poppins", Arial, sans-serif; font-size: 15.5px; color: var(--white);
    white-space: nowrap;
  }
  .tagline::before, .tagline::after {
    content: ""; flex: 1; height: 1px; background: var(--rule-light);
  }
</style>
</head>
<body>
<main class="canvas">
  <section class="card card--front" aria-label="Business card front">
    <div class="brand">
      <span class="brand__dot"></span>
      <span class="brand__name">MARWICK ESTATE<br>SERVICES</span>
    </div>

    <h1 class="holder">DANIEL HARLOW</h1>
    <div class="holder-rule"></div>

    <ul class="contacts">
      <li>
        <svg viewBox="0 0 16 16" aria-hidden="true"><path d="M4 0h8a1.5 1.5 0 0 1 1.5 1.5v13A1.5 1.5 0 0 1 12 16H4a1.5 1.5 0 0 1-1.5-1.5v-13A1.5 1.5 0 0 1 4 0zm0 2v10h8V2zm4 11a1 1 0 1 0 0 2 1 1 0 0 0 0-2z"/></svg>
        044-987 650 312
      </li>
      <li>
        <svg viewBox="0 0 16 16" aria-hidden="true"><path d="M3.6 1l2.3 3.1-1.4 1.6c.9 2 2.6 3.8 4.6 4.7l1.6-1.4L13.8 11l-1.5 2.7C7 13.6 2.4 9 2.2 3.7z"/><path d="M9.5 1.5a5 5 0 0 1 5 5h-1.3a3.7 3.7 0 0 0-3.7-3.7zm0 2.5A2.5 2.5 0 0 1 12 6.5h-1.2a1.3 1.3 0 0 0-1.3-1.3z"/></svg>
        044-987 650 312
      </li>
      <li>
        <svg viewBox="0 0 16 16" aria-hidden="true"><path d="M0 3h16v10H0zm1.6 1.2L8 9l6.4-4.8v-.1H1.6zM1.2 12h13.6L10 8l-2 1.5L6 8z"/></svg>
        hello@marwickestate.com
      </li>
    </ul>
    <div class="front-band"></div>
  </section>

  <section class="card card--back" aria-label="Business card back">
    <h2 class="slogan">
      <span class="slogan__lead">Your solution to all of your</span>
      <span class="slogan__main">Handyman and home</span>
      <span class="slogan__main">Improvement needs</span>
    </h2>
    <p class="tagline">Family Owned and Operated</p>
  </section>
</main>
</body>
</html>
```